Webdesign für IT Service Firma
Zielgruppe
Wir sind eine IT-Service Firma und bieten individuelle IT-Lösungen. Unsere Kunden sind KMU, also Firmen mit einer Grösse von 2-250 Mitarbeitern im Grossraum Basel, die in Ihrem Bereich Spezialisten sind und spezielle Anforderungen an Ihre IT besitzen.
Unsere USP sind fixe Ansprechpartner, gute Erreichbarkeit, schneller und individueller Service
Aufgabenstellung
Schriftart Myriad Pro
Grün: #7FA51D
Blau: #4D9BC2
Grau: #999999
Untertitel: Wir sind da.

```html
<!DOCTYPE html>
<html lang="de">
<head>
<meta charset="utf-8">
<title>KALOVA – IT-Security</title>
<link href="https://fonts.googleapis.com/css2?family=Work+Sans:wght@400;500;600;700&display=swap" rel="stylesheet">
<style>
:root{
  --green:#7fa51d;
  --green-soft:#e4edcf;
  --blue:#4d9bc2;
  --blue-dark:#2f6a8a;
  --nav-active:#2f6a8a;
  --grey:#999999;
  --text:#2b2b2b;
  --tint:#f6f9f0;
  --band:#eef1f5;
  --footer:#8399b0;
}
*{margin:0;padding:0;box-sizing:border-box}
html,body{width:853px;height:1200px;overflow:hidden}
body{position:relative;font-family:"Work Sans",Arial,sans-serif;color:var(--text);
  background:linear-gradient(160deg,#eef1f5 0%,#fbfcfd 40%,#eef1f5 100%)}
.abs{position:absolute}
.topbar a{color:var(--green);font-size:11px;text-decoration:none;display:flex;align-items:center;gap:7px}
.lang{font-size:6.5px;font-weight:700;color:var(--grey)}
.lang.active{color:var(--blue)}
.header{left:144px;top:45px;width:564px;height:56px;background:#fff;border-radius:4px 4px 0 0}
.logo{font-size:26px;font-weight:400;letter-spacing:-.5px;color:var(--blue)}
.tagline{left:463px;top:69px;font-size:10.5px;color:var(--blue);letter-spacing:.2px}
.skyline{left:578px;top:45px;width:130px;height:56px;border-radius:0 4px 0 0;
  background:linear-gradient(90deg,rgba(77,155,194,0) 0%,rgba(77,155,194,.35) 50%,rgba(77,155,194,.6) 100%)}
.nav{left:144px;top:101px;width:564px;height:30px;background:var(--blue);display:flex;padding-left:13px}
.nav a{color:#fff;font-weight:700;font-size:10.5px;text-decoration:none;padding:0 6px;line-height:30px;height:30px}
.nav a.active{background:var(--nav-active);height:33px;line-height:30px;padding:0 6px}
.hero-photo{left:60px;top:125px;width:320px;height:200px;
  background:radial-gradient(ellipse 50% 50% at 50% 45%,#8ea3b6 0%,#b7c4d0 45%,rgba(238,241,245,0) 100%)}
.hero-title{left:361px;top:180px;font-size:16.5px;line-height:23px;color:#1d1d1d;font-weight:400}
.hero-title b{color:var(--blue);font-weight:700}
.panel{left:125px;top:297px;width:603px;height:519px;background:#fff}
.tint{left:125px;top:453px;width:603px;height:169px;background:var(--tint)}
.icon{position:absolute;background:var(--green-soft);border-radius:4px}
.h2{position:absolute;left:245px;font-size:10.5px;font-weight:700;color:var(--blue-dark);line-height:15.5px}
.body{position:absolute;left:246px;width:266px;font-size:7.9px;line-height:11.6px;color:#222}
.body .link{color:var(--blue)}
.body .lead{color:var(--blue);font-weight:600}
.list{position:absolute;left:566px;list-style:none;font-size:7.8px;line-height:11.6px;color:var(--blue)}
.list li{position:relative;padding-left:11px}
.list li::before{content:"";position:absolute;left:0;top:3px;width:5px;height:5px;border:1.5px solid var(--blue-dark);border-radius:50%}
.band{left:0;top:815px;width:853px;height:171px;background:var(--band)}
.band-text{left:130px;top:850px;width:180px;text-align:center;font-size:11px;line-height:15.5px;color:var(--blue-dark)}
.cta{left:139px;top:894px;width:165px;height:46px;background:var(--blue-dark);color:#fff;font-size:11px;line-height:15.5px;padding:7px 0 0 28px;text-decoration:none}
.team-photo{left:326px;top:835px;width:204px;height:136px;
  background:radial-gradient(ellipse 50% 50% at 50% 50%,#c9d2dc 0%,#dde3ea 50%,rgba(238,241,245,0) 100%)}
.contact-title{left:560px;top:850px;width:130px;text-align:center;font-size:11px;color:var(--blue-dark)}
.portrait{width:57px;height:57px;background:linear-gradient(180deg,#dfe4ea 0%,#b9c2cc 100%)}
.pname{width:70px;text-align:center;font-size:7.8px;line-height:9.5px;color:var(--blue-dark)}
.footer{left:0;top:986px;width:853px;height:173px;background:var(--footer);color:#fff}
.f-block{position:absolute;left:184px;font-size:7.8px;line-height:11.5px}
.f-block strong{font-weight:700}
.f-icon{position:absolute;left:154px}
.f-head{position:absolute;left:344px;top:41px;font-size:7.8px;font-weight:700;letter-spacing:.3px}
.f-links{position:absolute;list-style:none;font-size:7.8px;line-height:17.7px}
.f-links li::before{content:"›";margin-right:6px;font-size:10px}
.bottom{left:0;top:1159px;width:853px;height:41px;background:#fff}
.bottom .logo{position:absolute;left:167px;top:10px;font-size:15px}
.legal{position:absolute;right:150px;top:17px;display:flex;gap:10px;font-size:7.8px}
.legal a{color:var(--blue);text-decoration:none}
</style>
</head>
<body>

<div class="topbar">
  <a class="abs" href="#" style="left:166px;top:15px">
    <svg width="13" height="13" viewBox="0 0 24 24" fill="none" stroke="#4d9bc2" stroke-width="1.6"><path d="M5 3l4 1 1 5-2 2a13 13 0 0 0 5 5l2-2 5 1 1 4-3 2C10 20 4 14 3 6z"/></svg>
    +41 61 480 2716</a>
  <a class="abs" href="#" style="left:289px;top:15px">
    <svg width="13" height="13" viewBox="0 0 24 24" fill="none" stroke="#4d9bc2" stroke-width="1.6"><rect x="2" y="5" width="20" height="14" rx="1"/><path d="M2 6l10 7 10-7"/></svg>
    support@kalova.ch</a>
  <span class="abs lang active" style="left:654px;top:19px">DE</span>
  <span class="abs lang" style="left:681px;top:19px">EN</span>
</div>

<div class="abs header"></div>
<div class="abs logo" style="left:166px;top:56px">KALOVA</div>
<div class="abs tagline">IT Services aus Basel</div>
<div class="abs skyline" role="img" aria-label="Stadtsilhouette von Basel mit Platinenlinien"></div>

<nav class="abs nav">
  <a href="#">Home</a><a href="#" class="active">Leistungen</a><a href="#">Privatkunde?</a><a href="#">Jobs</a><a href="#">Hilfe</a><a href="#">Sozialprozent</a><a href="#">Über uns</a><a href="#">Kontakt</a>
</nav>

<div class="abs hero-photo" role="img" aria-label="Foto: IT-Techniker vor mehreren Monitoren"></div>
<h1 class="abs hero-title">Wir bieten ganzheitliche <b>IT-Security</b><br>Lösungen für Ihr Unternehmen!</h1>

<div class="abs panel"></div>
<div class="abs tint"></div>

<div class="icon" style="left:167px;top:326px;width:44px;height:43px" role="img" aria-label="Illustration: Server mit Schloss"></div>
<h2 class="h2" style="top:323px">IT-Sicherheitscheck: Ihre IT auf dem Prüfstand</h2>
<p class="body" style="top:346px">Wir führen eine Risiko- und Sicherheitsanalyse Ihrer gesamten IT- und Kommunikations-Technik durch. Dabei betrachten wir produktneutral und herstellerübergreifend die bestehende oder neu geplante Infrastruktur und ermitteln das IT-Sicherheitsniveau. Gemeinsam besprechen wir vorhandene Sicherheitsprobleme und stellen einen Roadmap für deren Behebung auf.</p>
<ul class="list" style="top:330px">
  <li>Updatestand von Clients,<br>Servern, Firewall usw.</li>
  <li style="margin-top:8px">cryptosafe Backups/Archivierung</li>
  <li style="margin-top:10.5px">Monitoring</li>
  <li style="margin-top:10.5px">Auditierung</li>
</ul>

<div class="icon" style="left:167px;top:472px;width:44px;height:44px" role="img" aria-label="Illustration: Browserfenster mit Schloss"></div>
<h2 class="h2" style="top:467px">Website-Check</h2>
<p class="body" style="top:492px">Erhalten Sie eine unabhängige Meinung zum Sicherheitsstatus Ihrer Website oder Ihres Online-Shops: Wir prüfen auf Sicherheitslücken, Aktualität der verwendeten Software und Einhaltung aktueller Sicherheitsstandards.<br><br>Unter anderem verfügbar für: <span class="link">PressLeaf, PageCMS</span> und <span class="link">Cartwerk</span></p>
<ul class="list" style="top:477px">
  <li>Aktueller Updatestand &amp;<br>Lifecycle-Management</li>
  <li style="margin-top:8px">Korrekte Konfiguration, Absicherung<br>und Monitoring der Serversoftware</li>
  <li style="margin-top:8px">Verwendung sicherer Passwörter</li>
  <li style="margin-top:10.5px">Rechtssicherheit unter Achtung von<br>Datenschutz und Datensparsamkeit</li>
  <li style="margin-top:8px">Malware-Scan</li>
</ul>

<div class="icon" style="left:161px;top:656px;width:58px;height:36px" role="img" aria-label="Illustration: Schulung am Bildschirm"></div>
<h2 class="h2" style="top:648px">Security Awareness Training:<br>IT-Sicherheitsschulung für Ihre Mitarbeiter</h2>
<p class="body" style="top:688px">Das größte IT-Sicherheitsrisiko geht laut einer Studie von Securalis von den eigenen Mitarbeitern aus. Sei es durch Manipulation, Unachtsamkeit oder einfach Unwissenheit. In vielen Fällen erhalten Mitarbeiter keine ausreichend Schulung.<br><br><span class="lead">Praxisnah:</span> Wir zeigen, wie einfach Kriminelle Passwörter erbeuten, Computer übernehmen oder Geheimnisse entlocken können und bringen Ihren Mitarbeitern bei, wie man diese Versuche erkennt und sich richtig verhält.</p>
<ul class="list" style="top:656px">
  <li>Sichere Passwörter<br>(Passwortmanager)</li>
  <li style="margin-top:8px">Phishing erkennen und<br>Anti-Phishing-Tests</li>
  <li style="margin-top:8px">Datensicherheit</li>
</ul>

<div class="abs band"></div>
<p class="abs band-text">Das Training kann Online oder Inhouse durchgeführt werden.</p>
<a class="abs cta" href="#">Jetzt unverbindlich<br>Kontakt aufnehmen</a>
<div class="abs team-photo" role="img" aria-label="Foto: Mitarbeiterin mit Headset am Computer im Büro"></div>
<p class="abs contact-title">Ihre Ansprechpartner</p>
<div class="abs portrait" style="left:564px;top:886px" role="img" aria-label="Porträtfoto Ansprechpartner"></div>
<div class="abs portrait" style="left:635px;top:886px" role="img" aria-label="Porträtfoto Ansprechpartner"></div>
<p class="abs pname" style="left:557px;top:949px">Marco<br>Vobrak</p>
<p class="abs pname" style="left:628px;top:949px">Lukas<br>Brenner</p>

<footer class="abs footer">
  <svg class="f-icon" style="top:40px" width="17" height="20" viewBox="0 0 24 28" fill="none" stroke="#fff" stroke-width="1.8"><path d="M12 27s10-9 10-16a10 10 0 0 0-20 0c0 7 10 16 10 16z"/><circle cx="12" cy="11" r="4"/></svg>
  <p class="f-block" style="top:41px"><strong>KALOVA GmbH</strong><br>Lindenhofgasse 14<br>CH-4052 Basel</p>
  <svg class="f-icon" style="top:85px" width="17" height="17" viewBox="0 0 24 24" fill="none" stroke="#fff" stroke-width="1.6"><path d="M5 3l4 1 1 5-2 2a13 13 0 0 0 5 5l2-2 5 1 1 4-3 2C10 20 4 14 3 6z"/></svg>
  <p class="f-block" style="top:86px">Telefon<br>+41 61 480 2716</p>
  <svg class="f-icon" style="top:121px" width="17" height="15" viewBox="0 0 24 20" fill="none" stroke="#fff" stroke-width="1.8"><rect x="1" y="2" width="22" height="16"/><path d="M1 3l11 8 11-8"/></svg>
  <p class="f-block" style="top:120px">Email<br>support@kalova.ch</p>

  <p class="f-head">LEISTUNGEN</p>
  <ul class="f-links" style="left:345px;top:57px"><li>IT-Betreuung</li><li>IT-Sicherheit</li><li>Backup</li><li>Scientific IT</li></ul>
  <ul class="f-links" style="left:435px;top:57px"><li>Websites</li><li>Raumbuchung</li><li>Coworking Space / Sitzungszimmer</li><li>Home Office Lösungen</li></ul>
  <ul class="f-links" style="left:607px;top:57px"><li>Telefonie</li><li>Monitoring</li><li>Passwort Manager</li></ul>
</footer>

<div class="abs bottom">
  <span class="logo">KALOVA</span>
  <nav class="legal"><a href="#">Newsletter</a><a href="#">Datenschutz</a><a href="#">AGB</a><a href="#">Impressum</a></nav>
</div>

</body>
</html>
```